Business Card Design for Event Planning Company

Create a business card for event planning company using our new logo. After I pick the design, I will need files made for 6 employees. Our company provides event design & logistics services as well as venue management. The font should be sans serif and complementary to the logo. I will need to know the name of the font selected for the final design. The phone numbers listed should be separated by "." not "-"

Address for the card
PO Box 318, Washington, DC 20019

Card One
Lorna Pettibone
lpettibone@galavoyant.com
202.481.7730

Card Two
Miriam Okonkwo
mokonkwo@galavoyant.com
202.556.2047

Card Three
Tessa Varnholt
tvarnholt@galavoyant.com
978.620.4471

Card Four
Robin Fess
rfess@galavoyant.com
202.718.3362

Card Five
Ada-Rose Pelletan-Uzor
adarose@galavoyant.com
202.839.1205

Card Six
Beatrix Holloway
Beatrix@galavoyant.com
202.492.6618

Target Market(s)

Corporate/Non-Profit

Industry/Entity Type

Event Planning

Contact Information for Business Card

Address for the card

Card One
Lorna Pettibone
lpettibone@galavoyant.com
202.481.7730

Card Two
Miriam Okonkwo
202.556.2047

Card Three
Tessa Varnholt
978.620.4471

Card Four
Robin Fess
rfess@galavoyant.com
202.718.3362

Card Five
Ada-Rose Pelletan-Uzor
202.839.1205

Card Six
Beatrix Holloway
202.492.6618

Font styles to use
Sans Serif

Colors

Designer to choose colors to be used in the design.

Requirements
Must have
• Two-sided with logo
Should not have
• Extra colors or be too busy

```html
<!DOCTYPE html>
<html lang="en">
<head>
<meta charset="utf-8">
<title>Galavoyant Business Card</title>
<link href="https://fonts.googleapis.com/css2?family=Questrial&display=swap" rel="stylesheet">
<style>
  :root {
    --page-bg: #e6e6e6;
    --teal: #5f9fa0;
    --teal-text: #4f9496;
    --ink: #2f3434;
    --white: #ffffff;
    --card-back: #f7f7f7;
    --watermark: #e3e8e8;
    --rule: #2b3b3b;
  }
  * { margin: 0; padding: 0; box-sizing: border-box; }
  html, body {
    width: 1200px; height: 576px; overflow: hidden;
    background: var(--page-bg);
    font-family: "Questrial", "Century Gothic", sans-serif;
  }
  .stage { position: relative; width: 1200px; height: 576px; }

  .card {
    position: absolute; top: 138px; width: 485px; height: 292px;
    border-radius: 13px; overflow: hidden;
  }

  /* Front */
  .card-front { left: 82px; background: var(--teal); }
  .brand-mark {
    position: absolute; left: 50%; top: 90px; transform: translateX(-50%);
    width: 40px; height: 40px; border-radius: 50%; background: var(--white);
  }
  .brand-name {
    position: absolute; left: 0; right: 0; top: 140px;
    text-align: center; font-size: 41px; letter-spacing: 0.5px;
    color: var(--ink); line-height: 1;
  }
  .website {
    position: absolute; left: 0; right: 0; top: 256px;
    display: flex; align-items: center; justify-content: center; gap: 12px;
    font-size: 13px; color: var(--white);
  }
  .website .rule { width: 60px; height: 1px; background: var(--rule); }

  /* Back */
  .card-back { left: 602px; background: var(--card-back); }
  .watermark {
    position: absolute; left: 60px; top: 48px;
    width: 200px; height: 200px; border-radius: 50%;
    border: 30px solid var(--watermark);
  }
  .holder-name {
    position: absolute; left: 25px; top: 136px;
    font-size: 17px; color: var(--teal-text);
  }
  .contact {
    position: absolute; left: 238px; top: 120px;
    list-style: none; font-size: 13px; color: var(--ink); line-height: 16.5px;
  }
  .contact li { display: flex; align-items: center; gap: 9px; }
  .contact svg { width: 10px; height: 10px; fill: var(--teal-text); }
</style>
</head>
<body>
<main class="stage">
  <section class="card card-front" aria-label="Card front">
    <span class="brand-mark" aria-hidden="true"></span>
    <h1 class="brand-name">galavoyant</h1>
    <p class="website"><span class="rule"></span>www.galavoyant.com<span class="rule"></span></p>
  </section>

  <section class="card card-back" aria-label="Card back">
    <span class="watermark" aria-hidden="true"></span>
    <h2 class="holder-name">Beatrix Holloway</h2>
    <ul class="contact">
      <li><svg viewBox="0 0 10 10" aria-hidden="true"><path d="M1 3 Q5 0 9 3 L8 4.5 L6.5 3.8 L6.5 3 Q5 2.5 3.5 3 L3.5 3.8 L2 4.5 Z M2.5 5 H7.5 L8.5 9 H1.5 Z"/></svg>202.492.6618</li>
      <li><svg viewBox="0 0 10 10" aria-hidden="true"><path d="M0.5 2 H9.5 V8 H0.5 Z M1 2.5 L5 5.5 L9 2.5" /></svg>beatrix@galavoyant.com</li>
      <li style="margin-left:-8px">PO Box 318, Washington, DC 20019</li>
    </ul>
  </section>
</main>
</body>
</html>
```